Quorbeline.com.au - Managed online product sales programs, software platform and apps.

1. Sales & Distribution.We sell your products. On multiple websites, or to major retailers and independents, Clearance and job lots. We managed sales of products via our existing retail channels or a combination of .our channels and clients channels.
2. Software Applications. Use our platforms to manage the products, sales, tracking , customer service and more. Download our apps. Use of our platforms, like www.vaklur.com , or one of our many webstores, like shopnovari.com.au . Use of our apps for product management, sales, tracking and customer service notifications
3. Marketing .Omni channel Programs Online Marketing and SEO optimisation, to maximise your exposure. Marketing - SEO and strategies to increase sales and broaden exposure.

4. Consulting. Special projects and Custom work from advise, to software development. Consulting and Review - Specialised and customised work and business intelligence to improve clients business systems.

Target Market(s)

Target customers are either:
Wholesalers, i.e. companies who own warehouses of inventory and distribute products as wholesalers.
Retailers, i.e. companies operating multiple retail stores and now want to start an online sales program.
Dropship agents, i.e. people who act as brokers, selling products on behalf of wholesalers.
Freight and transport companies who need realtime tracking of products, during delivery from pickup aat warehouse through to delicery at customer.

Industry/Entity Type

Software

Colors

Designer to choose colors to be used in the design.

Requirements
Must have
• A. Simple home page without clutter. Just an easy registration and startup.
minimal menus.
B. Use of icons to indicate each of the 4 areas of work. Namely:
1. Sales - managed sales of products via our existing retail channels or a combination of .our channels and clients channels.
2. Software - use of our platforms, like www.vaklur.com , or one of our many webstores. Use of our apps for product management, sales, tracking and customer service notifications
3. Marketing - SEO and strategies to increase sales and broaden exposure.
4. Consulting and Review - Specialised and customised work and business intelligence to improve clients business systems.

C. Registration wizard to on-board a supplier in 3 easy steps, and start selling products. For example list on Trondlo in 2 easy steps.

D. Use of HTML5 for graphic interface, moving icons and images for a dynamic experience.

E. Internal app-store to download our own apps.

F. Graphical explanations instead of words.

G. Real images and photos
Should not have
• Many menus.
long winded wordy explanations.

```html
<!DOCTYPE html>
<html lang="en">
<head>
<meta charset="utf-8">
<title>Quorbeline – Managed Online Product Sales</title>
<link rel="stylesheet" href="https://fonts.googleapis.com/css2?family=Marcellus&family=Oswald:wght@400;500&family=Open+Sans:wght@400;600&display=swap">
<style>
  :root {
    --pink: #d6306e;
    --pink-light: #e15a8a;
    --ink: #1c1c1c;
    --text: #555;
    --muted: #888;
    --grey-bg: #e9e9e9;
    --footer-bg: #ececec;
    --white: #fff;
    --icon-grey: #9a9a9a;
    --store: #8a8a8a;
  }
  * { box-sizing: border-box; margin: 0; padding: 0; }
  html, body { width: 780px; height: 1200px; overflow: hidden; }
  body { position: relative; background: var(--white); font-family: "Open Sans", Arial, sans-serif; color: var(--text); }
  h1, h2, h3 { font-weight: 400; }
  .abs { position: absolute; }

  /* Hero */
  .hero { left: 0; top: 0; width: 780px; height: 388px;
    background: linear-gradient(90deg, #3a2c22 0%, #6a5240 35%, #7a5e44 60%, #a47a4e 80%, #5a4232 100%); }
  .hero-shade { left: 0; top: 0; width: 780px; height: 388px;
    background: linear-gradient(180deg, rgba(0,0,0,.15), rgba(0,0,0,0) 50%, rgba(190,140,80,.25)); }
  .navbar { left: 276px; top: 39px; width: 432px; height: 35px; background: var(--white);
    display: flex; align-items: center; padding: 0 10px; }
  .brand { font-family: "Oswald", sans-serif; font-weight: 500; font-size: 16px; letter-spacing: 1px; color: var(--ink); display: flex; align-items: center; gap: 5px; }
  .brand-mark { width: 9px; height: 9px; background: var(--pink); }
  .nav { margin-left: auto; display: flex; gap: 14px; list-style: none; }
  .nav li { font-family: "Oswald", sans-serif; font-size: 11.5px; color: var(--ink); }
  .nav li.active { color: var(--pink); }
  .hero-title { left: 276px; top: 110px; width: 420px; font-family: "Marcellus", serif; font-size: 21.5px; line-height: 28px; color: var(--white); }

  /* Welcome band */
  .welcome { left: 0; top: 388px; width: 780px; height: 72px; background: var(--pink); }
  .welcome-title { left: 164px; top: 402px; font-family: "Marcellus", serif; font-size: 15px; color: var(--white); }
  .welcome-text { left: 164px; top: 421px; width: 520px; font-size: 8px; line-height: 11px; color: var(--white); }

  /* Services */
  .services { left: 88px; top: 474px; width: 610px; height: 122px; display: flex; border-top: 3px solid #f3f3f6; }
  .service { flex: 1; padding: 16px 7px 0; border-right: 8px solid #f7f7fa; }
  .service:last-child { border-right: 0; }
  .service-head { display: flex; align-items: center; gap: 7px; margin-bottom: 6px; }
  .service-icon { width: 26px; height: 26px; border-radius: 50%; background: var(--icon-grey); display: flex; align-items: center; justify-content: center; }
  .service-title { font-size: 12px; color: #444; padding-top: 6px; }
  .service-text { font-size: 8px; line-height: 10px; color: var(--muted); }

  /* Register */
  .register { left: 0; top: 608px; width: 780px; height: 172px; background: var(--grey-bg); border-top: 2px solid #e0e0e0; }
  .register-title { left: 164px; top: 646px; font-family: "Marcellus", serif; font-size: 18px; color: #444; }
  .register-text { left: 164px; top: 671px; width: 520px; font-size: 8px; line-height: 10.5px; color: var(--text); }
  .step-btn { left: 164px; top: 715px; width: 93px; height: 24px; background: var(--pink); display: flex; }
  .step-play { width: 24px; height: 24px; background: var(--pink-light); display: flex; align-items: center; justify-content: center; }
  .step-label { flex: 1; text-align: center; font-family: "Marcellus", serif; font-size: 12px; line-height: 24px; color: var(--white); }

  /* Mobile */
  .mobile-photo { left: 72px; top: 810px; width: 338px; height: 269px; border-radius: 40px 40px 0 0;
    background: linear-gradient(160deg, #e7e2dc 0%, #c6b6a5 40%, #4a4e5a 75%, #2e323c 100%); }
  .mobile-title { left: 473px; top: 854px; font-family: "Marcellus", serif; font-size: 17px; line-height: 24px; color: #444; }
  .mobile-text { left: 418px; top: 915px; width: 270px; font-size: 10.5px; line-height: 12.5px; color: #444; }
  .store { top: 972px; width: 131px; height: 39px; background: var(--store); border-radius: 3px; color: var(--white);
    display: flex; flex-direction: column; justify-content: center; padding-left: 36px; }
  .store small { font-size: 7px; font-weight: 600; }
  .store strong { font-size: 15px; font-weight: 400; line-height: 16px; }
  .store-shape { position: absolute; left: 12px; top: 11px; width: 16px; height: 16px; background: var(--white); border-radius: 3px; }
  .store-a { left: 417px; }
  .store-b { left: 551px; }

  /* Footer */
  .footer { left: 0; top: 1079px; width: 780px; height: 121px; background: var(--footer-bg); }
  .footer-brand { left: 74px; top: 1110px; }
  .footer-about { left: 74px; top: 1143px; width: 160px; font-family: Arial, sans-serif; font-size: 7.5px; line-height: 9px; color: #777; }
  .footer-copy { left: 74px; top: 1165px; font-family: Arial, sans-serif; font-size: 7px; color: #333; }
  .footer-links { top: 1112px; list-style: none; font-family: Arial, sans-serif; font-size: 7.5px; line-height: 9.5px; color: #333; }
  .links-a { left: 287px; }
  .links-b { left: 372px; }
  .promo-label { left: 520px; top: 1111px; font-size: 9.5px; color: #444; }
  .signup { left: 517px; top: 1132px; width: 190px; height: 21px; background: var(--white); border: 1px solid #ddd; display: flex; }
  .signup span { flex: 1; font-family: Arial, sans-serif; font-size: 7.5px; line-height: 19px; padding-left: 8px; color: #888; }
  .signup b { width: 58px; background: var(--pink); color: var(--white); font-family: Arial, sans-serif; font-size: 7px; text-align: center; line-height: 19px; border-radius: 2px; }
  .social { left: 617px; top: 1159px; display: flex; gap: 6px; }
  .social i { width: 18px; height: 18px; border-radius: 50%; background: #333; display: block; }
</style>
</head>
<body>
  <div class="abs hero" role="img" aria-label="Photo of a man in shirt and tie using a tablet beside cardboard boxes in a warehouse"></div>
  <div class="abs hero-shade"></div>
  <header class="abs navbar">
    <div class="brand"><span>QUORBELINE</span><span class="brand-mark"></span></div>
    <ul class="nav">
      <li class="active">HOME</li><li>ABOUT US</li><li>CLIENTS</li><li>TESTIMONIALS</li><li>CONTACT US</li>
    </ul>
  </header>
  <h1 class="abs hero-title">MANAGED ONLINE PRODUCT SALES PROGRAMS, SOFTWARE PLATFORM AND APPS.</h1>

  <section class="abs welcome"></section>
  <svg class="abs" style="left:93px;top:400px" width="47" height="47" viewBox="0 0 47 47">
    <circle cx="23.5" cy="23.5" r="21.5" fill="none" stroke="#fff" stroke-width="2"/>
    <path d="M14 23.5h18M25 16l7.5 7.5L25 31" fill="none" stroke="#fff" stroke-width="3" stroke-linecap="round" stroke-linejoin="round"/>
  </svg>
  <h2 class="abs welcome-title">WELCOME TO QUORBELINE</h2>
  <p class="abs welcome-text">Lorem ipsum dolor sit amet, consectetur adipisicing elit, sed do eiusmod tempor incididunt ut labore et dolore magna aliqua. Ut enim ad minim veniam, quis nostrud exercitation ullamco laboris nisi ut aliquip ex ea commodo consequat.</p>

  <section class="abs services">
    <article class="service">
      <div class="service-head"><span class="service-icon"><svg width="14" height="12"><path d="M1 11h12M3 10V6M6 10V3M9 10V5M12 10V2" stroke="#fff" stroke-width="2"/></svg></span><h3 class="service-title">Sales</h3></div>
      <p class="service-text">Managed sales of products via our existing retail channels or a combination of .our channels and clients channels.</p>
    </article>
    <article class="service">
      <div class="service-head"><span class="service-icon"><svg width="14" height="14"><rect x="1" y="1" width="12" height="9" fill="none" stroke="#fff" stroke-width="1.6"/><path d="M5 13h4M7 10v3" stroke="#fff" stroke-width="1.6"/></svg></span><h3 class="service-title">Software</h3></div>
      <p class="service-text">Use of our apps for product management, sales, tracking and customer service notifications</p>
    </article>
    <article class="service">
      <div class="service-head"><span class="service-icon"><svg width="15" height="13"><rect x="1" y="1" width="13" height="8" fill="none" stroke="#fff" stroke-width="1.6"/><path d="M4 12l3.5-3 3.5 3" fill="none" stroke="#fff" stroke-width="1.4"/></svg></span><h3 class="service-title">Marketing</h3></div>
      <p class="service-text">SEO and strategies to increase sales and broaden exposure.</p>
    </article>
    <article class="service">
      <div class="service-head"><span class="service-icon"><svg width="14" height="14"><circle cx="4.5" cy="3" r="2" fill="#fff"/><circle cx="9.5" cy="3" r="2" fill="#fff"/><rect x="2" y="6" width="5" height="8" rx="1.5" fill="#fff"/><rect x="7.5" y="6" width="5" height="8" rx="1.5" fill="#fff"/></svg></span><h3 class="service-title">Consulting</h3></div>
      <p class="service-text">Specialised and customised work and business intelligence to improve clients business systems.</p>
    </article>
  </section>

  <section class="abs register"></section>
  <svg class="abs" style="left:93px;top:652px" width="47" height="47" viewBox="0 0 47 47">
    <circle cx="23.5" cy="23.5" r="21.5" fill="none" stroke="#d6306e" stroke-width="1.6"/>
    <rect x="15" y="16" width="17" height="11" fill="none" stroke="#d6306e" stroke-width="1.6"/>
    <path d="M12 30h23" stroke="#d6306e" stroke-width="1.6"/>
    <path d="M22 19l4 3.5-2 .3 1 2-1 .5-1-2-1 1.2z" fill="#d6306e"/>
  </svg>
  <h2 class="abs register-title">REGISTER NOW!</h2>
  <p class="abs register-text">Registration wizard to on-board a supplier in 3 easy steps Lorem ipsum dolor sit amet, consectetur adipisicing elit, sed do eiusmod tempor incididunt ut labore et dolore magna aliqua. Ut enim ad minim veniam, quis nostrud exercitation ullamco laboris nisi ut aliquip ex ea commodo consequat.</p>
  <div class="abs step-btn">
    <span class="step-play"><svg width="8" height="9"><path d="M0 0l8 4.5L0 9z" fill="#fff"/></svg></span>
    <span class="step-label">STEP 1</span>
  </div>

  <div class="abs mobile-photo" role="img" aria-label="Photo of a young man with a shoulder bag looking at his phone, beside a hand holding a smartphone showing the site"></div>
  <svg class="abs" style="left:417px;top:855px" width="47" height="47" viewBox="0 0 47 47">
    <circle cx="23.5" cy="23.5" r="21.5" fill="none" stroke="#d6306e" stroke-width="1.6"/>
    <rect x="16" y="17" width="10" height="16" rx="1.5" fill="none" stroke="#d6306e" stroke-width="1.6"/>
    <rect x="22" y="12" width="12" height="8" rx="3" fill="#d6306e"/>
    <circle cx="21" cy="30" r="1" fill="#d6306e"/>
  </svg>
  <h2 class="abs mobile-title">MOBILE AND TABLET<br>CONNECTIVITY</h2>
  <p class="abs mobile-text">Receive alerts on your smartphone &amp; tablet whenever motion is detected. Connect live with two-way audio and streaming video.</p>
  <div class="abs store store-a"><span class="store-shape"></span><small>GET THE APP ON</small><strong>Playvault</strong></div>
  <div class="abs store store-b"><span class="store-shape"></span><small>Available on the</small><strong>Appdock</strong></div>

  <footer class="abs footer"></footer>
  <div class="abs brand footer-brand"><span>QUORBELINE</span><span class="brand-mark" style="background:#888"></span></div>
  <p class="abs footer-about">Lorem ipsum dolor sit amet, consectetur adipisicing elit ang mga ibon.</p>
  <p class="abs footer-copy">Copyright © 2013. All Rights Reserved</p>
  <ul class="abs footer-links links-a"><li>Home</li><li>About Us</li><li>Blog</li><li>Clients</li><li>How It Works</li></ul>
  <ul class="abs footer-links links-b"><li>Contact</li><li>Privacy Policy</li><li>Terms of Service</li><li>Support</li><li>Security</li></ul>
  <p class="abs promo-label">Get promos, giveaways and company news:</p>
  <div class="abs signup"><span>Email Address</span><b>Subscribe</b></div>
  <div class="abs social"><i></i><i></i><i></i><i></i></div>
</body>
</html>
```